stationary deign for trucking company

im a trucking company looking for a professional set of stationary designs i deliver goods from point a to b
Updates

When submitting stationary designs I need envelope design, letterhead, cards, I’d badge etc

Industry/Entity Type

Trucking Company

Requirements
Must have
• must have letter head, business card, envelope, fax sheet, id badge, folder, thank you card, notebook, invoice sheet.
Nice to have
• nice to have them all custom made (letterhead,envelope, business card, I’d badge etc
Should not have
• must not have prepaid sign want i unique design for items

```html
<!DOCTYPE html>
<html lang="en">
<head>
<meta charset="utf-8">
<title>Brentwood Transportation – Letterhead &amp; Envelope</title>
<link href="https://fonts.googleapis.com/css2?family=Montserrat:wght@500;600&family=Arimo:wght@400&display=swap" rel="stylesheet">
<style>
  :root {
    --brand-blue: #1a5aa8;
    --band-grey: #d3d3d3;
    --ink: #1d1d1f;
    --paper: #ffffff;
    --canvas: #ffffff;
  }
  * { box-sizing: border-box; margin: 0; padding: 0; }
  html, body { width: 1200px; height: 1200px; overflow: hidden; background: var(--canvas); }
  .stage { position: relative; width: 1200px; height: 1200px; }

  .sheet {
    position: absolute;
    background: var(--paper);
    box-shadow: 14px 16px 26px rgba(0,0,0,0.28);
    overflow: hidden;
  }
  .letterhead { left: 65px; top: 68px; width: 821px; height: 1063px; }
  .envelope   { left: 405px; top: 512px; width: 753px; height: 376px; }

  .spine { position: absolute; top: 0; bottom: 0; background: var(--brand-blue); }
  .letterhead .spine { left: 49px; width: 39px; }
  .envelope .spine   { left: 41px; width: 184px; }

  .header-band { position: absolute; left: 0; }
  .header-band polygon { fill: var(--band-grey); }
  .letterhead .header-band { top: 60px; }
  .envelope .header-band { top: 57px; }

  .brand { position: absolute; display: flex; align-items: center; }
  .brand-mark { background: var(--brand-blue); flex: none; }
  .brand-text { display: flex; flex-direction: column; }
  .brand-name {
    font-family: "Montserrat", sans-serif; font-weight: 600;
    color: var(--ink); letter-spacing: 0.04em; line-height: 1; white-space: nowrap;
  }
  .brand-tagline {
    font-family: "Montserrat", sans-serif; font-weight: 600;
    color: var(--ink); letter-spacing: 0.2em; line-height: 1; white-space: nowrap;
  }
  .letterhead .brand { left: 105px; top: 76px; gap: 20px; }
  .letterhead .brand-mark { width: 18px; height: 18px; }
  .letterhead .brand-name { font-size: 27px; }
  .letterhead .brand-tagline { font-size: 7.5px; margin-top: 6px; }
  .envelope .brand { left: 63px; top: 71px; gap: 14px; }
  .envelope .brand-mark { width: 14px; height: 14px; }
  .envelope .brand-name { font-size: 19px; }
  .envelope .brand-tagline { font-size: 5.5px; margin-top: 3px; letter-spacing: 0.17em; }

  .contact { position: absolute; font-family: "Arimo", sans-serif; }
  .contact-text { position: absolute; white-space: nowrap; line-height: 1.2; }
  .contact-icon {
    position: absolute; display: flex; align-items: center; justify-content: center;
    border-radius: 2px;
  }
  .contact-icon svg { display: block; }
  .contact-icon svg * { fill: none; stroke-width: 1.4; }

  .letterhead .contact { left: 0; top: 0; color: var(--ink); font-size: 13.5px; }
  .letterhead .contact-text { left: 100px; }
  .letterhead .contact-icon { left: 61px; width: 15px; height: 15px; background: var(--paper); }
  .letterhead .contact-icon svg * { stroke: var(--brand-blue); }

  .envelope .contact { left: 0; top: 0; color: #fff; font-size: 11px; }
  .envelope .contact-text { left: 60px; }
  .envelope .contact-icon { left: 29px; width: 13px; height: 12px; background: var(--brand-blue); }
  .envelope .contact-icon svg * { stroke: #fff; }
</style>
</head>
<body>
<div class="stage">

  <section class="sheet letterhead" aria-label="Letterhead">
    <div class="spine"></div>
    <svg class="header-band" width="520" height="64" viewBox="0 0 520 64"><polygon points="0,0 520,0 454,64 0,64"/></svg>
    <div class="brand">
      <span class="brand-mark"></span>
      <div class="brand-text">
        <span class="brand-name">BRENTWOOD</span>
        <span class="brand-tagline">TRANSPORTATION • LOGISTICS</span>
      </div>
    </div>
    <div class="contact">
      <span class="contact-icon" style="top:917px"><svg width="11" height="11" viewBox="0 0 11 11"><circle cx="5.5" cy="5.5" r="4"/></svg></span>
      <span class="contact-text" style="top:916px">YOUR ADDRESS HERE</span>
      <span class="contact-text" style="top:934px">12345</span>
      <span class="contact-icon" style="top:960px"><svg width="11" height="11" viewBox="0 0 11 11"><path d="M5.5 10 C3 7 2.5 5.5 2.5 4.5 a3 3 0 0 1 6 0 C8.5 5.5 8 7 5.5 10Z"/></svg></span>
      <span class="contact-text" style="top:958px">000111222</span>
      <span class="contact-icon" style="top:979px"><svg width="11" height="11" viewBox="0 0 11 11"><rect x="3" y="1.5" width="5" height="8" rx="0.8"/></svg></span>
      <span class="contact-text" style="top:977px">info@brentwoodhaulers.com</span>
      <span class="contact-icon" style="top:998px"><svg width="11" height="11" viewBox="0 0 11 11"><rect x="1.5" y="2.5" width="8" height="6"/><path d="M1.5 2.5 L5.5 6 L9.5 2.5"/></svg></span>
      <span class="contact-text" style="top:996px">brentwoodhaulers.com</span>
    </div>
  </section>

  <section class="sheet envelope" aria-label="Envelope">
    <div class="spine"></div>
    <svg class="header-band" width="720" height="52" viewBox="0 0 720 52"><polygon points="0,0 720,0 664,52 0,52"/></svg>
    <div class="brand">
      <span class="brand-mark"></span>
      <div class="brand-text">
        <span class="brand-name">BRENTWOOD</span>
        <span class="brand-tagline">TRANSPORTATION • LOGISTICS</span>
      </div>
    </div>
    <div class="contact">
      <span class="contact-icon" style="top:252px"><svg width="9" height="9" viewBox="0 0 11 11"><circle cx="5.5" cy="5.5" r="4"/></svg></span>
      <span class="contact-text" style="top:251px">YOUR ADDRESS HERE</span>
      <span class="contact-text" style="top:265px">12345</span>
      <span class="contact-icon" style="top:287px"><svg width="9" height="9" viewBox="0 0 11 11"><path d="M5.5 10 C3 7 2.5 5.5 2.5 4.5 a3 3 0 0 1 6 0 C8.5 5.5 8 7 5.5 10Z"/></svg></span>
      <span class="contact-text" style="top:286px">000111222</span>
      <span class="contact-icon" style="top:303px"><svg width="9" height="9" viewBox="0 0 11 11"><rect x="3" y="1.5" width="5" height="8" rx="0.8"/></svg></span>
      <span class="contact-text" style="top:302px">info@brentwoodhaulers.com</span>
      <span class="contact-icon" style="top:319px"><svg width="9" height="9" viewBox="0 0 11 11"><rect x="1.5" y="2.5" width="8" height="6"/><path d="M1.5 2.5 L5.5 6 L9.5 2.5"/></svg></span>
      <span class="contact-text" style="top:317px">brentwoodhaulers.com</span>
    </div>
  </section>

</div>
</body>
</html>
```